Corvane Business Cards & Staionary
Corvane, Inc.
Project: Corvane Business Cards & Staionary
Corvane Business Cards & Staionary - Real Estate
Creative Brief
Professional
Leonard T. Haskovich
President
418 W. Thornberry Blvd. Harlow, FL 33590
len@corvanetx.com

```html
<!DOCTYPE html>
<html lang="en">
<head>
<meta charset="utf-8">
<title>Corvane, Inc. — Business Cards</title>
<link rel="stylesheet" href="https://fonts.googleapis.com/css2?family=Libre+Baskerville:wght@400;700&family=Cormorant+SC:wght@500;600&display=swap">
<style>
  :root{
    --stage-top:#f4f4f4;
    --stage-bottom:#d9d9d9;
    --gold-light:#e8c56c;
    --gold:#c9962f;
    --gold-dark:#9b6d1b;
    --ink:#3b3d48;
    --paper:#ffffff;
    --shadow:rgba(0,0,0,.22);
  }
  *{margin:0;padding:0;box-sizing:border-box}
  html,body{width:1200px;height:874px;overflow:hidden}
  body{
    background:radial-gradient(ellipse at 50% 40%,var(--stage-top) 0%,var(--stage-bottom) 100%);
    position:relative;
    font-family:"Cormorant SC","Times New Roman",serif;
  }
  .card{
    position:absolute;
    width:560px;height:320px;
    border-radius:26px;
    overflow:hidden;
    box-shadow:0 14px 30px var(--shadow);
    background:var(--paper);
  }
  .card-art{position:absolute;inset:0;width:100%;height:100%}

  /* Back */
  .card-back{left:580px;top:90px}
  .back-web{
    position:absolute;right:34px;top:92px;
    color:var(--paper);font-size:15px;letter-spacing:3px;font-weight:600;
  }
  .back-brand{
    position:absolute;left:150px;top:150px;
    display:flex;align-items:center;gap:12px;
    font-family:"Libre Baskerville","Times New Roman",serif;
    font-weight:700;font-size:34px;color:var(--ink);
  }
  .back-brand .mark{width:22px;height:22px;background:var(--ink)}

  /* Front */
  .card-front{left:80px;top:460px}
  .front-brand{
    position:absolute;left:40px;top:40px;width:260px;text-align:center;
  }
  .brand-name{
    font-family:"Libre Baskerville","Times New Roman",serif;
    font-weight:700;font-size:30px;color:var(--ink);
  }
  .brand-tagline{
    margin-top:6px;font-size:10px;letter-spacing:1px;color:var(--gold-dark);font-weight:600;
  }
  .contact-list{
    position:absolute;left:22px;top:196px;list-style:none;
  }
  .contact-list li{
    display:flex;align-items:center;gap:7px;
    color:var(--paper);font-size:12px;line-height:17px;letter-spacing:.5px;font-weight:600;
  }
  .contact-list svg{width:11px;height:11px;flex:none}
  .person{
    position:absolute;right:40px;top:232px;text-align:right;color:var(--paper);
  }
  .person-name{font-size:19px;font-weight:600;letter-spacing:1px}
  .person-title{font-size:12px;letter-spacing:2px;margin-top:2px;font-weight:600}
</style>
</head>
<body>

<section class="card card-back" aria-label="Business card, back">
  <svg class="card-art" viewBox="0 0 560 320" preserveAspectRatio="none" aria-hidden="true">
    <defs>
      <linearGradient id="goldBack" x1="0" y1="0" x2="1" y2="1">
        <stop offset="0" stop-color="var(--gold-dark)"/>
        <stop offset=".45" stop-color="var(--gold-light)"/>
        <stop offset="1" stop-color="var(--gold)"/>
      </linearGradient>
    </defs>
    <rect width="560" height="320" fill="url(#goldBack)"/>
    <path d="M0 210 C110 250 230 280 330 320 L0 320 Z" fill="var(--paper)"/>
    <path d="M0 198 C120 240 240 272 350 320" fill="none" stroke="var(--paper)" stroke-width="3"/>
  </svg>
  <div class="back-web">WWW.CORVANETX.COM</div>
  <div class="back-brand"><span class="mark"></span>Corvane, Inc.</div>
</section>

<section class="card card-front" aria-label="Business card, front">
  <svg class="card-art" viewBox="0 0 560 320" preserveAspectRatio="none" aria-hidden="true">
    <defs>
      <linearGradient id="goldFront" x1="0" y1="0" x2="1" y2="1">
        <stop offset="0" stop-color="var(--gold)"/>
        <stop offset=".5" stop-color="var(--gold-light)"/>
        <stop offset="1" stop-color="var(--gold-dark)"/>
      </linearGradient>
    </defs>
    <path d="M0 178 C160 130 330 210 560 112 L560 320 L0 320 Z" fill="url(#goldFront)"/>
    <path d="M0 166 C160 118 330 198 560 100" fill="none" stroke="var(--gold)" stroke-width="2"/>
    <path d="M0 186 C160 140 330 218 560 122" fill="none" stroke="var(--paper)" stroke-width="3"/>
  </svg>

  <div class="front-brand">
    <div class="brand-name">Corvane, Inc.</div>
    <div class="brand-tagline">Residential &amp; Commercial Property Services</div>
  </div>

  <ul class="contact-list">
    <li><svg viewBox="0 0 12 12"><circle cx="6" cy="6" r="6" fill="#fff"/><path d="M6 2.5a2 2 0 0 1 2 2c0 1.6-2 4.5-2 4.5S4 6.1 4 4.5a2 2 0 0 1 2-2z" fill="#c9962f"/></svg>418 W. Thornberry Blvd.</li>
    <li><svg viewBox="0 0 12 12"><circle cx="6" cy="6" r="6" fill="#fff"/></svg>Harlow, FL 33590</li>
    <li><svg viewBox="0 0 12 12"><circle cx="6" cy="6" r="6" fill="#fff"/><path d="M4 3h1.3l.6 1.6-.8.6a4 4 0 0 0 1.7 1.7l.6-.8 1.6.6V8A1 1 0 0 1 8 9 5 5 0 0 1 3 4a1 1 0 0 1 1-1z" fill="#c9962f"/></svg>(555) 014-2287</li>
    <li><svg viewBox="0 0 12 12"><circle cx="6" cy="6" r="6" fill="#fff"/><path d="M4 3h1.3l.6 1.6-.8.6a4 4 0 0 0 1.7 1.7l.6-.8 1.6.6V8A1 1 0 0 1 8 9 5 5 0 0 1 3 4a1 1 0 0 1 1-1z" fill="#c9962f"/></svg>(555) 014-2288</li>
    <li><svg viewBox="0 0 12 12"><circle cx="6" cy="6" r="6" fill="#fff"/><rect x="3" y="4" width="6" height="4" fill="none" stroke="#c9962f"/><path d="M3 4l3 2.2L9 4" fill="none" stroke="#c9962f"/></svg>len@corvanetx.com</li>
    <li><svg viewBox="0 0 12 12"><circle cx="6" cy="6" r="6" fill="#fff"/><circle cx="6" cy="6" r="3" fill="none" stroke="#c9962f"/><path d="M3 6h6M6 3v6" stroke="#c9962f"/></svg>www.corvanetx.com</li>
  </ul>

  <div class="person">
    <div class="person-name">Leonard T. Haskovich</div>
    <div class="person-title">President</div>
  </div>
</section>

</body>
</html>
```